Design a modern, classy & professional business card for an online real estate agency, specializing in medium-luxury properties in Thailand and later in Singapore and UK.

Possible design ideas so far: (not essential)

- curved corner(s) to the card, white on front & turquoise on back or visa versa.

- front of card - clear and simple, company name in metallic grey/monochrome, logo graphic & company name on front in spot UV or embossed/debossed effect.

- back of card - large, close-cropped, 'ghost' patterns of the C-shaped curves of logo, or company name repeated on back of card in spot UV.

Target Market(s)

- young to middle-aged professionals mainly (but ideally should design should suit all)

- UK, US,EU,AUS & ASIAN mainly (but ideally should design should suit all countries)

Industry/Entity Type

Real Estate

Requirements
Must have
• THEME:
- Luxurious & Modern
- Clean & striking
- Unique & creative

INFO:
- Logo & company name on front
- Contact details on back:

Tobias Lindqvist
Managing Director

www.velmoraestates.example
www.velmoraestates-uk.example

Tel: 083-274-6190
email: tobias@velmoraestates.example

(contact details can be displayed in any order as suites design.)

Nice to have
• - curved corner(s) to the card, white on front & turquoise on back or visa versa.

Should not have
• - No generic images of properties, palm trees/coconut trees etc.

- No other other bold colors, except for main turquoise, grey, metallic white & black theme.

- No obvious business card templates

```html
<!DOCTYPE html>
<html lang="en">
<head>
<meta charset="utf-8">
<title>Velmora Estates – Business Card</title>
<link rel="stylesheet" href="https://fonts.googleapis.com/css2?family=Marcellus&display=swap">
<style>
  :root {
    --backdrop: #b9c0c0;
    --card-white: #ffffff;
    --turquoise: #55f8b8;
    --slate: #5f6a70;
    --ink: #4a4f52;
    --text-font: "Marcellus", serif;
  }
  * { margin: 0; padding: 0; box-sizing: border-box; }
  html, body {
    width: 1200px;
    height: 900px;
    overflow: hidden;
  }
  body {
    background: var(--backdrop);
    font-family: var(--text-font);
    position: relative;
  }
  .card {
    position: absolute;
    left: 320px;
    width: 560px;
    height: 320px;
    background: var(--card-white);
    border-radius: 6px;
    box-shadow: 0 6px 18px rgba(0,0,0,0.18);
    overflow: hidden;
  }
  .card-front { top: 110px; }
  .card-back { top: 470px; }

  /* Front */
  .brand {
    position: absolute;
    left: 64px;
    top: 128px;
    display: flex;
    align-items: center;
    gap: 22px;
  }
  .brand-square {
    width: 64px;
    height: 64px;
    background: var(--turquoise);
  }
  .brand-name {
    font-size: 46px;
    color: var(--slate);
    letter-spacing: 0.5px;
    line-height: 1;
  }

  /* Back */
  .name-band {
    position: absolute;
    left: 0;
    top: 0;
    width: 100%;
    height: 168px;
    background: var(--turquoise);
  }
  .holder-name {
    position: absolute;
    left: 152px;
    top: 62px;
    font-size: 32px;
    color: var(--card-white);
  }
  .holder-title {
    position: absolute;
    left: 152px;
    top: 110px;
    font-size: 21px;
    color: var(--card-white);
    letter-spacing: 1px;
  }
  .contact {
    position: absolute;
    left: 30px;
    top: 196px;
    color: var(--ink);
    font-size: 14px;
    line-height: 19px;
  }
  .contact-block + .contact-block { margin-top: 10px; }
</style>
</head>
<body>
  <section class="card card-front" aria-label="Card front">
    <div class="brand">
      <div class="brand-square"></div>
      <div class="brand-name">Velmora Estates</div>
    </div>
  </section>

  <section class="card card-back" aria-label="Card back">
    <div class="name-band"></div>
    <div class="holder-name">Tobias Lindqvist</div>
    <div class="holder-title">MANAGING DIRECTOR</div>
    <div class="contact">
      <div class="contact-block">
        <p>Tel: 083-274-6190</p>
        <p>email: tobias@velmoraestates.example</p>
      </div>
      <div class="contact-block">
        <p>www.velmoraestates.example</p>
        <p>www.velmoraestates-uk.example</p>
      </div>
    </div>
  </section>
</body>
</html>
```